Website Design Needed for Performance Horse Trading Business

We require a website designed for Saddlemire, a new business which lists top quality performance stock horse bloodlines for sale. Our Australian company caters to the Australian Stock Horse, Quarter Horse and Paint Horse breeds of horse used for performance events such as Camp drafting and Cutting. The website design needs to communicate quality, have a professional look while maintaining a western, rural feel.
Colour schemes that we are looking for are either grey and orange, navy and grey or brown and grey.
The logo for the website has been attached below
Design deliverables are as follows:
-Main Page
-Horses for Sale Page
-Horse Listing Page
-Html & CSS files for pages
MAIN PAGE
----------------
Description: This page is where customers land, search for horses, see premium horses
Elements which need to be included on the main page are
-a horse filter section, allowing customers to search for horse listings by filtering attributes.
-premium listings displaying large photos of horse, price and location.
Horses for Sale PAGE
---------------------------------
Description: This page displays a list of available horses for sale as per the filtered results.
Elements which need to be included on this page are
- a filter panel which allows customers to filter results
- list of horses available for sale
Horse Listing Page
-------------------------------
Description: This page displays all the information about the horse for sale.
Screenshots of the basic program are attached for the Horses for Sale Page and the Horse Listing Page to give an idea of the elements required ONLY and should not be thought of as a design guideline.
Webpage HEADER
-------------------------
The Header section of the website should include login/signup buttons, 'my account' buttons (or links) as well as a featured link/button that says 'Sell Your Horse'
Updates
Thank you all for your designs so far. We would like to see the Sell Your Horse section featured more in the website design to attract customers. This would be as a button or highlighted link that is eye catching in the primary section of the website design of the main page. Perhaps placing it on the right hand side adjacent to the search function lets customers make the mental decision as to whether they are looking to buy or looking to sell when they visit the website. The wording above or near the button would be 'Advertise your horse with us' with the words on the button being 'Create Ad!'.
Industry/Entity Type
Events
Look and feel
Each slider illustrates characteristics of the customer's brand and the style your logo design should communicate.

```html
<!DOCTYPE html>
<html lang="en">
<head>
<meta charset="utf-8">
<title>Saddlemire – Performance Stock Horses</title>
<link href="https://fonts.googleapis.com/css2?family=Roboto:wght@300;400;500;700&family=Lobster&display=swap" rel="stylesheet">
<style>
  :root {
    --orange: #f07a26;
    --orange-light: #f58d4c;
    --orange-dark: #d9661a;
    --charcoal: #3b3b3b;
    --charcoal-dark: #2c2c2c;
    --peach: #fbd9c2;
    --band-grey: #b5adaa;
    --forest: #1f2a1c;
    --text: #333333;
    --muted: #777777;
    --line: #dddddd;
    --footer-bg: #eeeeee;
    --white: #ffffff;
  }
  * { box-sizing: border-box; margin: 0; padding: 0; }
  html, body { width: 791px; height: 1200px; overflow: hidden; }
  body {
    position: relative;
    font-family: "Roboto", Arial, sans-serif;
    color: var(--text);
    background: var(--white);
  }
  .abs { position: absolute; }

  /* Hero background */
  .hero-bg {
    left: 0; top: 0; width: 791px; height: 369px;
    background: radial-gradient(ellipse at 50% 40%, #ffffff 0%, #fff6f0 40%, var(--peach) 100%);
  }

  /* Header */
  .brand {
    left: 114px; top: 24px;
    font-family: "Roboto", sans-serif; font-weight: 700; font-size: 24px;
    color: var(--charcoal-dark); letter-spacing: 0.5px;
    display: flex; align-items: center; gap: 6px;
  }
  .brand-mark { width: 10px; height: 10px; background: var(--orange); }
  .account-btn {
    top: 26px; height: 22px; font-size: 9px; color: var(--white);
    display: flex; align-items: center; justify-content: center;
    border-bottom: 2px solid rgba(0,0,0,0.25);
  }
  .account-btn.dark { background: var(--charcoal); left: 488px; width: 77px; }
  .account-btn.login { background: var(--orange); left: 570px; width: 52px; }
  .account-btn.signup { background: var(--orange); left: 627px; width: 51px; }

  .main-nav {
    left: 113px; top: 73px; width: 565px; height: 39px;
    display: flex; background: var(--orange);
    box-shadow: 0 6px 6px -4px rgba(0,0,0,0.35);
  }
  .main-nav a {
    display: flex; align-items: center; justify-content: center;
    color: var(--white); text-decoration: none; font-size: 9.5px;
    border-right: 1px solid rgba(0,0,0,0.12);
  }
  .main-nav .home { width: 58px; background: var(--orange-light); }
  .main-nav .sell {
    margin-left: auto; width: 112px; font-weight: 500;
    background: linear-gradient(#4a4a4a, var(--charcoal-dark)); border: 0;
  }

  /* Hero */
  .hero-photo {
    left: 328px; top: 124px; width: 344px; height: 264px;
    background: radial-gradient(ellipse at 55% 45%, #b5662a 0%, #8a4a1c 45%, rgba(255,255,255,0) 72%);
  }
  .slide-arrow { top: 190px; }
  .slide-arrow.prev { left: 64px; }
  .slide-arrow.next { left: 708px; }
  .hero-title { left: 148px; top: 226px; font-size: 18px; color: var(--orange); font-weight: 400; }
  .hero-sub { left: 144px; top: 250px; font-size: 13px; color: var(--charcoal-dark); }
  .learn-btn {
    left: 144px; top: 274px; width: 75px; height: 24px;
    background: var(--charcoal); color: var(--white); font-size: 8px;
    border-radius: 4px; display: flex; align-items: center; justify-content: center;
  }

  /* Search band */
  .search-band { left: 0; top: 369px; width: 791px; height: 65px; background: var(--band-grey); }
  .search-label {
    left: 113px; top: 369px; width: 125px; height: 65px; background: var(--charcoal);
    font-family: "Lobster", cursive; font-size: 19px; line-height: 21px;
    padding: 11px 0 0 26px; color: var(--white);
  }
  .search-label span { color: var(--orange); display: block; }
  .search-label svg { position: absolute; left: 94px; top: 24px; }
  .select {
    top: 389px; height: 28px; background: var(--white); border: 1px solid #cccccc;
    font-size: 8px; color: #666; padding: 0 0 0 10px; display: flex; align-items: center;
  }
  .select.category { left: 260px; width: 157px; }
  .select.keywords { left: 428px; width: 156px; }
  .select .caret {
    position: absolute; right: 0; top: -1px; width: 22px; height: 28px; background: var(--orange);
    display: flex; align-items: center; justify-content: center;
  }
  .search-btn {
    left: 610px; top: 389px; width: 60px; height: 27px; background: var(--orange);
    color: var(--white); font-size: 8.5px; border-radius: 2px;
    display: flex; align-items: center; justify-content: center;
  }

  /* Premium */
  .premium {
    left: 0; top: 434px; width: 791px; height: 235px;
    background: linear-gradient(180deg, #2a2a26 0%, #1d2b18 60%, #2a3a22 100%);
  }
  .premium-title {
    left: 0; top: 448px; width: 791px; text-align: center;
    font-family: "Lobster", cursive; font-size: 18px; color: var(--white);
  }
  .premium-panel { left: 114px; top: 482px; width: 564px; height: 169px; background: rgba(70,70,70,0.85); }
  .premium-arrow { top: 560px; }
  .card {
    top: 500px; width: 123px; height: 134px; background: var(--white);
  }
  .card .photo { position: absolute; left: 5px; top: 4px; width: 113px; height: 82px; }
  .card .name { position: absolute; left: 0; top: 95px; width: 100%; text-align: center; font-size: 7.5px; color: #444; }
  .card .price { position: absolute; left: 16px; top: 113px; font-size: 7.5px; color: #e0502a; }
  .card .pin {
    position: absolute; right: 16px; top: 109px; width: 18px; height: 18px; border-radius: 50%;
    background: var(--orange); display: flex; align-items: center; justify-content: center;
  }

  /* Featured */
  .featured-title { left: 114px; top: 688px; font-family: "Lobster", cursive; font-size: 19px; color: var(--orange); }
  .feature-photo {
    width: 166px; height: 96px; border: 3px solid var(--white);
    box-shadow: 0 0 0 1px #cccccc;
  }
  .feature-text { width: 390px; }
  .feature-text h3 { font-size: 13px; font-weight: 400; color: var(--charcoal-dark); margin-bottom: 8px; }
  .feature-text p { font-size: 7.2px; line-height: 12.4px; color: var(--muted); margin-bottom: 4px; }
  .feature-text .meta { font-size: 8px; color: #555; margin-top: 5px; }
  .feature-text .meta b { font-size: 11px; font-weight: 400; color: var(--orange); }
  .divider { left: 113px; width: 566px; height: 1px; background: var(--line); }

  /* Footer */
  .footer { left: 0; top: 1104px; width: 791px; height: 96px; background: var(--footer-bg); border-top: 2px solid #cccccc; }
  .footer-brand {
    left: 116px; top: 1140px; font-weight: 700; font-size: 17px; color: var(--charcoal-dark);
    display: flex; align-items: center; gap: 5px;
  }
  .footer-brand i { width: 8px; height: 8px; background: var(--orange); display: block; }
  .social { top: 1126px; width: 30px; height: 30px; border: 1px solid #444; border-radius: 50%; }
  .copyright { left: 0; top: 1169px; width: 797px; text-align: center; font-size: 8px; color: #444; }
  .contact { left: 575px; font-size: 8px; color: #333; display: flex; align-items: center; gap: 5px; }
</style>
</head>
<body>

  <div class="abs hero-bg"></div>

  <!-- Header -->
  <div class="abs brand"><span>Saddlemire</span><i class="brand-mark"></i></div>
  <div class="abs account-btn dark">MY ACCOUNT</div>
  <div class="abs account-btn login">LOGIN</div>
  <div class="abs account-btn signup">SIGNUP</div>

  <nav class="abs main-nav">
    <a class="home" href="#">HOME</a>
    <a href="#" style="width:87px">ABOUT US</a>
    <a href="#" style="width:94px">OUR HORSES</a>
    <a href="#" style="width:80px">FOR SALE</a>
    <a href="#" style="width:62px">BLOG</a>
    <a href="#" style="width:70px">CONTACT</a>
    <a class="sell" href="#">SELL YOUR HORSE</a>
  </nav>

  <!-- Hero slider -->
  <div class="abs hero-photo" role="img" aria-label="Bay Australian Stock Horse standing in profile"></div>
  <svg class="abs slide-arrow prev" width="20" height="42" viewBox="0 0 20 42"><path d="M19 1 L1 21 L19 41" fill="none" stroke="#222" stroke-width="1.2"/></svg>
  <svg class="abs slide-arrow next" width="20" height="42" viewBox="0 0 20 42"><path d="M1 1 L19 21 L1 41" fill="none" stroke="#222" stroke-width="1.2"/></svg>
  <div class="abs hero-title">AUSTRALIAN STOCK HORSE</div>
  <div class="abs hero-sub">QUARTER HORSE AND PAINT HORSE</div>
  <div class="abs learn-btn">LEARN MORE</div>

  <!-- Search -->
  <div class="abs search-band"></div>
  <div class="abs search-label">Search<span>Horses</span>
    <svg width="12" height="20" viewBox="0 0 12 20"><path d="M2 2 L10 10 L2 18" fill="none" stroke="#fff" stroke-width="1.6"/></svg>
  </div>
  <div class="abs select category">Category
    <span class="caret"><svg width="8" height="5"><path d="M0 0 H8 L4 5Z" fill="#fff"/></svg></span>
  </div>
  <div class="abs select keywords">Keywords
    <span class="caret"><svg width="8" height="5"><path d="M0 0 H8 L4 5Z" fill="#fff"/></svg></span>
  </div>
  <div class="abs search-btn">SEARCH</div>

  <!-- Premium horses -->
  <div class="abs premium" role="img" aria-label="Dark background photo of a horse grazing on green pasture"></div>
  <div class="abs premium-title">Premium Horses</div>
  <div class="abs premium-panel"></div>
  <svg class="abs premium-arrow" style="left:123px" width="9" height="17" viewBox="0 0 9 17"><path d="M8 1 L1 8.5 L8 16" fill="none" stroke="#fff" stroke-width="1.2"/></svg>
  <svg class="abs premium-arrow" style="left:663px" width="9" height="17" viewBox="0 0 9 17"><path d="M1 1 L8 8.5 L1 16" fill="none" stroke="#fff" stroke-width="1.2"/></svg>

  <div class="abs card" style="left:143px">
    <div class="photo" role="img" aria-label="Australian Stock Horse on grass" style="background:linear-gradient(#c9d9c0,#6f9a4c)"></div>
    <div class="name">AUSTRALIAN STOCK HORSE</div>
    <div class="price">$50.00</div>
    <div class="pin"><svg width="8" height="10" viewBox="0 0 8 10"><path d="M4 9.5 C1 6 0.6 4.6 0.6 3.6 A3.4 3.4 0 0 1 7.4 3.6 C7.4 4.6 7 6 4 9.5Z" fill="none" stroke="#fff" stroke-width="1"/><circle cx="4" cy="3.6" r="1.1" fill="#fff"/></svg></div>
  </div>
  <div class="abs card" style="left:271px">
    <div class="photo" role="img" aria-label="Palomino Quarter Horse" style="background:linear-gradient(135deg,#3a2a1a,#c9782e 60%,#e8a560)"></div>
    <div class="name">QUARTER HORSE</div>
    <div class="price">$50.00</div>
    <div class="pin"><svg width="8" height="10" viewBox="0 0 8 10"><path d="M4 9.5 C1 6 0.6 4.6 0.6 3.6 A3.4 3.4 0 0 1 7.4 3.6 C7.4 4.6 7 6 4 9.5Z" fill="none" stroke="#fff" stroke-width="1"/><circle cx="4" cy="3.6" r="1.1" fill="#fff"/></svg></div>
  </div>
  <div class="abs card" style="left:399px">
    <div class="photo" role="img" aria-label="Black and white Paint Horse in a paddock" style="background:linear-gradient(#b6c0a8,#5d6a4a 55%,#7f8a62)"></div>
    <div class="name">PAINT HORSE</div>
    <div class="price">$50.00</div>
    <div class="pin"><svg width="8" height="10" viewBox="0 0 8 10"><path d="M4 9.5 C1 6 0.6 4.6 0.6 3.6 A3.4 3.4 0 0 1 7.4 3.6 C7.4 4.6 7 6 4 9.5Z" fill="none" stroke="#fff" stroke-width="1"/><circle cx="4" cy="3.6" r="1.1" fill="#fff"/></svg></div>
  </div>
  <div class="abs card" style="left:527px">
    <div class="photo" role="img" aria-label="Chestnut Quarter Horse trotting in a field" style="background:linear-gradient(#d5e2ee,#b07a4c 55%,#6f9a4c)"></div>
    <div class="name">QUARTER HORSE</div>
    <div class="price">$50.00</div>
    <div class="pin"><svg width="8" height="10" viewBox="0 0 8 10"><path d="M4 9.5 C1 6 0.6 4.6 0.6 3.6 A3.4 3.4 0 0 1 7.4 3.6 C7.4 4.6 7 6 4 9.5Z" fill="none" stroke="#fff" stroke-width="1"/><circle cx="4" cy="3.6" r="1.1" fill="#fff"/></svg></div>
  </div>

  <!-- Featured horses -->
  <div class="abs featured-title">Featured Horses</div>

  <div class="abs feature-photo" style="left:116px;top:726px;background:linear-gradient(#6f8f4e,#5f8a3a 50%,#8fb060)" role="img" aria-label="White horse in a green paddock"></div>
  <div class="abs feature-text" style="left:294px;top:725px">
    <h3>Suspendisse quam molestie sed</h3>
    <p>Lorem Ipsum has been the industry's standard dummy text ever since the 1500s, when an unknown printer took a galley of type and scrambled it to make a type specimen book. It has survived not only five centuries, but also the leap into electronic typesetting, remaining essentially unchanged.</p>
    <div class="meta">Location:&nbsp; New York</div>
    <div class="meta">Price: <b>$5000</b></div>
  </div>
  <div class="abs divider" style="top:836px"></div>

  <div class="abs feature-photo" style="left:114px;top:850px;background:linear-gradient(90deg,#5a3a22,#8a6a44 45%,#d9c48e)" role="img" aria-label="Close view of a bay horse in a dry field"></div>
  <div class="abs feature-text" style="left:292px;top:849px">
    <h3>Curabitur iaculis tempus eros</h3>
    <p>Lorem Ipsum has been the industry's standard dummy text ever since the 1500s, when an unknown printer took a galley of type and scrambled it to make a type specimen book. It has survived not only five centuries, but also the leap into electronic typesetting, remaining essentially unchanged.</p>
    <div class="meta">Location:&nbsp; New York</div>
    <div class="meta">Price: <b>$5000</b></div>
  </div>
  <div class="abs divider" style="top:958px"></div>

  <div class="abs feature-photo" style="left:112px;top:973px;background:linear-gradient(#8aa860,#6d5a34 55%,#b8a870)" role="img" aria-label="Brown horse galloping across a meadow"></div>
  <div class="abs feature-text" style="left:290px;top:971px">
    <h3>Ut nisi erat fermentum</h3>
    <p>Lorem Ipsum has been the industry's standard dummy text ever since the 1500s, when an unknown printer took a galley of type and scrambled it to make a type specimen book. It has survived not only five centuries, but also the leap into electronic typesetting, remaining essentially unchanged.</p>
    <div class="meta">Location:&nbsp; New York</div>
    <div class="meta">Price: <b>$5000</b></div>
  </div>

  <!-- Footer -->
  <footer class="abs footer"></footer>
  <div class="abs footer-brand"><span>Saddlemire</span><i></i></div>
  <div class="abs social" style="left:337px" aria-label="Social link"></div>
  <div class="abs social" style="left:381px" aria-label="Social link"></div>
  <div class="abs social" style="left:425px" aria-label="Social link"></div>
  <div class="abs copyright">Copyright © 2014 , All rights reserved.</div>
  <div class="abs contact" style="top:1140px;left:596px">
    <svg width="10" height="10" viewBox="0 0 10 10"><circle cx="5" cy="5" r="4.4" fill="none" stroke="#f07a26"/><path d="M3.2 2.8 L4.2 2.6 L4.6 3.8 L4 4.3 Q4.6 5.5 5.7 6 L6.2 5.4 L7.4 5.8 L7.2 6.8 Q4 7 3.2 2.8Z" fill="#f07a26"/></svg>
    +61-2-5550-1842
  </div>
  <div class="abs contact" style="top:1156px;left:575px">
    <svg width="10" height="8" viewBox="0 0 10 8"><rect width="10" height="8" fill="#f07a26"/><path d="M0.5 0.8 L5 4.4 L9.5 0.8" fill="none" stroke="#fff" stroke-width="0.9"/></svg>
    hello@saddlemire.example
  </div>

</body>
</html>
```